Corvell Advisory

Business Development Consulting Firm

Target Market(s)

Federal Government, 8(a) companies, Small Businesses

Industry/Entity Type

Private Sector, US Government

Contact Information for Business Card

8(a) Program Capture, Business Development, Industry Trends & Analysis, Strategic Teaming, Cyber Solutions

Colors

Designer to choose colors to be used in the design.

```html
<!DOCTYPE html>
<html lang="en">
<head>
<meta charset="utf-8">
<title>Corvell Advisory – Business Cards</title>
<link href="https://fonts.googleapis.com/css2?family=Lato:wght@300;400;700;900&display=swap" rel="stylesheet">
<style>
  :root {
    --cyan: #12aed1;
    --orange: #f7a81b;
    --ink: #555a60;
    --paper: #ffffff;
    --backdrop: #2c2c2e;
  }
  * { box-sizing: border-box; margin: 0; padding: 0; }
  html, body {
    width: 1200px; height: 689px; overflow: hidden;
    background: var(--backdrop);
    font-family: "Lato", Arial, sans-serif;
  }
  .card {
    position: absolute; top: 193px;
    width: 530px; height: 303px;
    border-radius: 16px; overflow: hidden;
  }

  /* Front */
  .card--front { left: 50px; background: var(--cyan); color: var(--paper); }
  .front-brand {
    position: absolute; left: 0; right: 0; top: 92px;
    text-align: center;
  }
  .front-brand .brand-name {
    display: inline-flex; align-items: center; gap: 14px;
    font-size: 44px; font-weight: 400; letter-spacing: 2px;
    text-transform: uppercase; line-height: 1;
  }
  .front-brand .brand-dot {
    width: 18px; height: 18px; border-radius: 50%; background: var(--paper);
  }
  .front-brand .brand-tagline {
    margin-top: 12px;
    font-size: 10.5px; letter-spacing: 3.2px; text-transform: uppercase; font-weight: 400;
  }
  .services {
    position: absolute; left: 0; right: 0; bottom: 30px;
    text-align: center; font-size: 11.5px; font-weight: 700; letter-spacing: .2px;
  }

  /* Back */
  .card--back { left: 620px; background: var(--paper); color: var(--ink); }
  .back-brand {
    position: absolute; right: 30px; top: 34px; text-align: right;
  }
  .back-brand .brand-name {
    display: inline-flex; align-items: center; gap: 10px;
    font-size: 26px; font-weight: 400; letter-spacing: 1.4px;
    text-transform: uppercase; color: var(--cyan); line-height: 1;
  }
  .back-brand .brand-dot { width: 12px; height: 12px; border-radius: 50%; background: var(--cyan); }
  .back-brand .brand-tagline {
    margin-top: 7px; font-size: 6.5px; font-weight: 700;
    letter-spacing: 1.6px; text-transform: uppercase; color: var(--ink);
  }
  .rule { position: absolute; height: 1px; background: var(--cyan); }
  .rule--top { left: 260px; right: 30px; top: 100px; }
  .rule--name { left: 30px; width: 220px; top: 186px; }

  .person { position: absolute; left: 30px; top: 130px; }
  .person-name { font-size: 24px; font-weight: 900; color: var(--cyan); letter-spacing: .5px; line-height: 1; }
  .person-title { margin-top: 6px; font-size: 14px; color: var(--orange); }

  .contacts { position: absolute; left: 34px; top: 196px; list-style: none; }
  .contacts li { display: flex; align-items: center; gap: 9px; font-size: 11.5px; line-height: 17px; }
  .contacts svg { width: 11px; height: 11px; fill: var(--orange); flex: none; }

  .address {
    position: absolute; right: 30px; top: 112px; text-align: right;
    font-size: 11.5px; line-height: 17px;
  }
  .address .company { color: var(--orange); font-size: 12.5px; }

  .footer-band { position: absolute; left: 0; bottom: 0; width: 530px; height: 48px; }
</style>
</head>
<body>

<section class="card card--front" aria-label="Business card front">
  <div class="front-brand">
    <div class="brand-name"><span class="brand-dot"></span>Corvell Advisory</div>
    <div class="brand-tagline">Business Development Consulting Firm</div>
  </div>
  <p class="services">Program Capture | Business Development | Industry Trends &amp; Analysis | Strategic Teaming</p>
</section>

<section class="card card--back" aria-label="Business card back">
  <div class="back-brand">
    <div class="brand-name"><span class="brand-dot"></span>Corvell Advisory</div>
    <div class="brand-tagline">Business Development Consulting Firm</div>
  </div>
  <div class="rule rule--top"></div>

  <div class="person">
    <div class="person-name">DANA WHITFIELD</div>
    <div class="person-title">Founder &amp; CEO</div>
  </div>
  <div class="rule rule--name"></div>

  <ul class="contacts">
    <li><svg viewBox="0 0 16 16"><path d="M3 1l3 3-2 2c1 2 3 4 5 5l2-2 3 3-2 3C6 14 2 10 1 3z"/></svg>(555) 014-2280</li>
    <li><svg viewBox="0 0 16 16"><path d="M4 0h8v16H4zM5.5 2v10h5V2zM7 13h2v1.5H7z" fill-rule="evenodd"/></svg>(555) 014-2281</li>
    <li><svg viewBox="0 0 16 16"><path d="M4 1h8v4H4zM1 6h14v6h-3v3H4v-3H1zM5 10v3h6v-3z" fill-rule="evenodd"/></svg>(555) 014-2282</li>
    <li><svg viewBox="0 0 16 16"><path d="M0 3h16v10H0zM1.5 4.5L8 9l6.5-4.5z" fill-rule="evenodd"/></svg>info@corvelladvisory.com</li>
  </ul>

  <address class="address" style="font-style:normal">
    <div class="company">Corvell Advisory Group</div>
    <div>4870 Linden Court, Ste 210</div>
    <div>Hartwell, CT 06012</div>
    <div>www.corvelladvisory.com</div>
  </address>

  <svg class="footer-band" viewBox="0 0 530 48" preserveAspectRatio="none" aria-hidden="true">
    <polygon points="0,38 420,38 420,48 0,48" fill="var(--cyan)"/>
    <polygon points="420,10 424,10 424,48 420,48" fill="var(--cyan)"/>
    <polygon points="428,8 530,0 530,48 428,48" fill="var(--orange)"/>
  </svg>
</section>

</body>
</html>
```